"Green Shopper Award" sales presentation

UK: "Shopper Award Green" is a French label, rewarding the best organic product sold in hyper and supermarkets. We already did the presentation in PPT format. But it is not design and professional-looking enough. The idea is that you use the existing document, and do not change anything in the structure, content, and text: you only have to improve the design (using the appropriate color code). We thank you in advance for any suggestion! FR: "Palme Acheteurs Vert" is a French distinction that rewards the best organic products sold in supermarkets and hypermarkets. The sales pitch is already done in PPT version. However, he still does not look pretty design / professional. Thus, we do not want you to modify the content, the structure, the images, but simply that you make it more design (following the appropriate graphic). Thank you in advance for your feedback!

Target Market(s)

Organic brands and supermarkets / organic brands and supermarkets

Requirements
Must have
• Follow the structure of the PPT made available (see attachment), keep the structure and the content, but improve the design - ideally with illustrator Ideally use Illustrator (Adobe) to improve the design of the current presentation - purpose keep the same content and structure
Nice to have
• You can use Illustrator ideally (or photoshop) to rework the design of the PPT

```html
<!DOCTYPE html>
<html lang="fr">
<head>
<meta charset="utf-8">
<title>Palme Acheteurs Vert – présentation commerciale</title>
<link href="https://fonts.googleapis.com/css2?family=Nunito+Sans:wght@400;600;700&family=Lora:wght@400&display=swap" rel="stylesheet">
<style>
:root{--pink:#ec1b63;--pink-mid:#f46a9a;--pink-soft:#f9b9cf;--pink-pale:#fde3ec;--ink:#3a3a3a;--grey:#8f9297;--frame:#9b9fa4;--teal:#3fd7b3;--dark:#3b3b3d;--wood:#d7a06a;--paper:#fff}
*{box-sizing:border-box;margin:0;padding:0}
html,body{width:1200px;height:1130px;overflow:hidden}
body{background:var(--frame);font-family:"Nunito Sans",sans-serif;color:var(--ink);position:relative}
.slide{position:absolute;width:383px;height:216px;background:var(--paper);overflow:hidden}
.abs{position:absolute}
.hd{position:absolute;left:10px;top:12px;display:flex;align-items:center;gap:6px;font-size:14px;color:var(--ink);white-space:nowrap}
.hd em{font-style:normal;color:var(--pink)}
.mark{width:16px;height:16px;background:var(--pink);flex:none}
.hd-bar{position:absolute;left:0;top:10px;width:4px;height:20px;background:var(--pink)}
.ft{position:absolute;right:8px;bottom:5px;font-size:5px;color:var(--grey);display:flex;align-items:center;gap:2px;text-transform:uppercase}
.ft i{width:5px;height:5px;border-radius:50%;border:1px solid var(--grey)}
.logo{display:flex;flex-direction:column;align-items:center;gap:3px;color:var(--pink);font-weight:700;text-align:center;line-height:1.05}
.logo .sq{width:34px;height:34px;border:3px solid var(--pink);border-radius:6px}
.toc{position:absolute;list-style:none;font-size:5.5px}
.toc li{display:flex;align-items:center;height:17px}
.toc b{font-family:Lora,serif;font-weight:400;color:var(--pink);font-size:10px;width:22px}
.brands{position:absolute;display:grid;gap:5px}
.brand{height:24px;border-radius:4px;background:var(--paper);color:var(--pink);font-size:6px;font-weight:700;display:flex;align-items:center;justify-content:center;text-align:center;line-height:1;border:1px solid var(--pink-soft)}
.ph{position:absolute;background:linear-gradient(135deg,#6d4a3a,#c9b6a6);}
.ph.room{background:linear-gradient(160deg,#d9d4cc,#6e6a66)}
.txt{font-size:4px;line-height:1.35;color:var(--ink)}
.pinkbox{background:var(--pink-mid);color:#fff;font-size:4px;line-height:1.35;text-align:center;padding:4px 6px}
.hex{position:absolute;width:40px;height:44px;clip-path:polygon(50% 0,100% 25%,100% 75%,50% 100%,0 75%,0 25%);background:var(--pink);display:flex;align-items:center;justify-content:center}
.hex::before{content:"";position:absolute;inset:5px;clip-path:inherit;background:#fff}
.hex span{position:relative;width:12px;height:9px;border:1.5px solid var(--pink-mid);border-radius:1px}
.card{position:absolute;top:70px;width:62px;height:110px;border:1px solid var(--pink);border-radius:7px;overflow:hidden;text-align:center}
.card .band{height:10px}
.card .ic{width:14px;height:10px;margin:6px auto 4px;border:1.5px solid}
.card p{font-size:3.6px;line-height:1.35;padding:0 4px;color:var(--pink-mid)}
.board{position:absolute;border:5px solid var(--wood);background:#f4f1ee;padding:4px}
.board h4{background:var(--pink-soft);color:#fff;font-size:5px;text-align:center;padding:3px;margin-bottom:5px}
.board p{font-size:3.6px;line-height:1.35;margin-bottom:6px;text-align:center}
.wbox{position:absolute;border:1px solid #ddd;background:#fff;font-size:3.8px;line-height:1.35;text-align:center;padding:5px 6px;box-shadow:0 1px 2px rgba(0,0,0,.15)}
</style>
</head>
<body>

<!-- 1 cover -->
<section class="slide" style="left:10px;top:11px">
  <svg class="abs" width="383" height="216" viewBox="0 0 383 216">
    <polygon points="0,0 383,0 383,6 118,216 0,216" fill="#ec1b63"/>
    <polygon points="383,6 383,30 148,216 118,216" fill="#f9b9cf"/>
    <circle cx="197" cy="107" r="62" fill="#e9e9ea"/>
    <circle cx="197" cy="107" r="50" fill="#fff"/>
  </svg>
  <div class="logo abs" style="left:162px;top:80px;width:70px;font-size:9px"><span class="sq"></span>Palme Acheteurs Vert</div>
  <p class="abs" style="left:110px;top:182px;width:190px;text-align:center;font-size:10px;line-height:1.3">PALME ACHETEURS VERT<br>2019</p>
  <div class="ft"><i></i>Verdania</div>
</section>

<!-- 2 cover variant -->
<section class="slide" style="left:406px;top:11px">
  <svg class="abs" width="383" height="216" viewBox="0 0 383 216">
    <polygon points="302,0 383,0 383,216 150,216" fill="#ec1b63"/>
    <polygon points="290,0 302,0 150,216 138,216" fill="#3b3b3d"/>
  </svg>
  <p class="abs" style="left:78px;top:48px;font-size:4px;color:var(--grey)">○ VERDANIA</p>
  <div class="logo abs" style="left:70px;top:58px;width:60px;font-size:8px"><span class="sq"></span>Palme Acheteurs Vert</div>
  <p class="abs" style="left:20px;top:132px;width:160px;text-align:center;font-size:10.5px;line-height:1.15">PALME<br>ACHETEURS VERT<br>2019</p>
</section>

<!-- 3 sommaire -->
<section class="slide" style="left:804px;top:11px">
  <div class="hd"><span class="mark"></span>Sommaire</div>
  <ol class="toc" style="left:12px;top:64px">
    <li><b>01</b>Palme Acheteurs Vert, c'est quoi?</li><li><b>02</b>Une certification d'excellence</li><li><b>03</b>Qui peut concourir?</li><li><b>04</b>Le déroulement du concours</li><li><b>05</b>Participer, c'est...</li><li><b>06</b>La visibilité des lauréats</li><li><b>07</b>Inscription</li>
  </ol>
  <div class="abs" style="left:202px;top:0;width:181px;height:216px;background:var(--pink)"></div>
  <div class="abs" style="left:210px;top:8px;width:165px;height:200px;border:1px solid var(--pink-soft)"></div>
  <p class="abs" style="left:215px;top:34px;width:156px;text-align:center;color:#fff;font-size:7px;font-style:italic;line-height:1.3">Les marques participantes de l'édition 2018</p>
  <div class="brands" style="left:212px;top:92px;width:160px;grid-template-columns:1fr 1fr 1fr">
    <div class="brand">Plantessa</div><div class="brand" style="border-radius:50%;width:24px;justify-self:center">Tô Bio</div><div class="brand">Rucher Doré</div>
    <div class="brand">Fournil Vert</div><div class="brand" style="border-radius:50%;width:30px;justify-self:center">Miel Lunaire</div><div class="brand">Potager Clair</div>
    <div class="brand">Adelis</div><div></div><div class="brand">Bonsoir Prairie</div>
  </div>
  <div class="ft" style="left:16px;right:auto"><i></i>Verdania</div>
</section>

<!-- 4 sommaire pink -->
<section class="slide" style="left:10px;top:234px;background:var(--pink)">
  <div class="hd" style="color:#fff"><span class="mark" style="background:#fff"></span>Sommaire</div>
  <div class="abs" style="left:6px;top:38px;width:210px;height:170px;background:#fff"></div>
  <svg class="abs" style="left:180px;top:38px" width="200" height="170" viewBox="0 0 200 170"><polygon points="0,0 168,0 198,85 168,170 0,170" fill="#fbd0df"/></svg>
  <ol class="toc" style="left:12px;top:64px">
    <li><b>01</b>Palme Acheteurs Vert, c'est quoi?</li><li><b>02</b>Une certification d'excellence</li><li><b>03</b>Qui peut concourir?</li><li><b>04</b>Le déroulement du concours</li><li><b>05</b>Participer, c'est...</li><li><b>06</b>La visibilité des lauréats</li><li><b>07</b>Inscription</li>
  </ol>
  <p class="abs" style="left:212px;top:50px;width:150px;text-align:center;color:var(--ink);font-size:7px;font-style:italic;line-height:1.3">Les marques participantes de l'édition 2018</p>
  <div class="brands" style="left:200px;top:86px;width:150px;grid-template-columns:1fr 1fr 1fr">
    <div class="brand">Plantessa</div><div class="brand" style="border-radius:50%;width:24px;justify-self:center">Tô Bio</div><div class="brand">Rucher Doré</div>
    <div class="brand">Fournil Vert</div><div></div><div class="brand">Potager Clair</div>
    <div class="brand">Adelis</div><div class="brand" style="border-radius:50%;width:30px;justify-self:center">Miel Lunaire</div><div class="brand">Bonsoir Prairie</div>
  </div>
  <div class="ft" style="left:16px;right:auto;color:#fff"><i style="border-color:#fff"></i>Verdania</div>
</section>

<!-- 5 sommaire timeline -->
<section class="slide" style="left:406px;top:234px">
  <div class="hd-bar"></div>
  <div class="hd"><span class="mark"></span>Sommaire</div>
  <div class="abs" style="left:19px;top:48px;width:1px;height:130px;background:var(--pink-soft)"></div>
  <div class="abs" style="left:12px;top:62px">
    <svg width="16" height="120" viewBox="0 0 16 120">
      <circle cx="8" cy="8" r="7" fill="#ec1b63"/><circle cx="8" cy="25" r="7" fill="#ec1b63"/>
      <circle cx="8" cy="42" r="7" fill="#f46a9a"/><circle cx="8" cy="59" r="7" fill="#f79cbd"/>
      <circle cx="8" cy="76" r="7" fill="#f9b9cf"/><circle cx="8" cy="93" r="7" fill="#fbd0df"/><circle cx="8" cy="110" r="7" fill="#fde3ec"/>
    </svg>
  </div>
  <ol class="toc" style="left:35px;top:62px">
    <li>Palme Acheteurs Vert, c'est quoi?</li><li>Une certification d'excellence</li><li>Qui peut concourir?</li><li>Le déroulement du concours</li><li>Participer, c'est...</li><li>La visibilité des lauréats</li><li>Inscription</li>
  </ol>
  <p class="abs" style="left:228px;top:22px;width:130px;text-align:center;color:var(--pink);font-size:7px;font-style:italic;line-height:1.3">Les marques participantes de l'édition 2018</p>
  <div class="brands" style="left:185px;top:48px;width:190px;grid-template-columns:repeat(3,1fr)">
    <div></div><div class="brand">Rucher Doré</div><div class="brand">Plantessa</div>
    <div class="brand">Fournil Vert</div><div class="brand" style="border-radius:50%;width:26px;justify-self:center">Tô Bio</div><div class="brand">Potager Clair</div>
    <div class="brand">Adelis</div><div class="brand" style="border-radius:50%;width:32px;justify-self:center">Miel Lunaire</div><div class="brand">Bonsoir Prairie</div>
  </div>
  <div class="ft"><i></i>Verdania</div>
</section>

<!-- 6 c'est quoi -->
<section class="slide" style="left:804px;top:234px">
  <div class="hd-bar"></div>
  <div class="hd"><span class="mark"></span>Palme Acheteurs Vert, <em>c'est quoi?</em></div>
  <div class="wbox" style="left:30px;top:48px;width:80px;height:48px;text-align:left">C'est la distinction de consommateurs réservée aux produits bio commercialisés en grandes et moyennes surfaces.</div>
  <div class="wbox" style="left:30px;top:102px;width:80px;height:50px;text-align:left">Ce concours distingue les produits bio et écologiques aux meilleures notes afin d'encourager l'excellence dans ce secteur et guider les achats.</div>
  <div class="wbox" style="left:30px;top:158px;width:80px;height:50px;text-align:left">Elle permet d'identifier les produits d'excellence de la filière biologique en circuit GMS, de les valoriser et d'augmenter leur notoriété.</div>
  <div class="logo abs" style="left:117px;top:106px;width:40px;font-size:5px"><span class="sq" style="width:26px;height:26px"></span>Palme Acheteurs Vert</div>
  <div class="abs" style="left:169px;top:60px;width:1px;height:150px;background:var(--pink-soft)"></div>
  <div class="abs" style="left:268px;top:44px;width:110px;height:102px;background:var(--pink-soft);clip-path:polygon(25% 0,75% 0,100% 50%,75% 100%,25% 100%,0 50%)"></div>
  <div class="abs" style="left:278px;top:52px;width:90px;height:86px;background:#fff"></div>
  <svg class="abs" style="left:282px;top:64px" width="82" height="60" viewBox="0 0 82 60">
    <rect x="0" y="4" width="8" height="50" fill="#f46a9a"/>
    <rect x="14" y="6" width="62" height="4" fill="#5bc0de"/><rect x="14" y="16" width="34" height="4" fill="#5bc0de"/>
    <rect x="14" y="26" width="30" height="4" fill="#5bc0de"/><rect x="14" y="36" width="26" height="4" fill="#5bc0de"/><rect x="14" y="46" width="22" height="4" fill="#5bc0de"/>
  </svg>
  <div class="wbox" style="left:182px;top:138px;width:118px;height:66px;border:1px solid var(--pink);text-align:left;border-radius:3px">La distinction Palme Acheteurs Vert est calquée sur le même modèle qu'une distinction déjà reconnue en grande distribution. Elle est dédiée au seul circuit GMS, lancée en 2018, et déjà plébiscitée par les consommateurs.</div>
  <div class="ft"><i></i>Verdania</div>
</section>

<!-- 7 excellence hexagons -->
<section class="slide" style="left:10px;top:456px">
  <div class="hd-bar"></div>
  <div class="hd"><span class="mark"></span>Une certification <em>d'excellence</em></div>
  <div class="hex" style="left:36px;top:92px;background:var(--pink-soft)"><span></span></div>
  <div class="hex" style="left:99px;top:72px"><span></span></div>
  <div class="hex" style="left:162px;top:56px"><span style="border:none;width:auto;height:auto;font-size:6px;color:var(--pink-mid)">15/20</span></div>
  <div class="hex" style="left:225px;top:72px"><span></span></div>
  <div class="hex" style="left:293px;top:92px;background:var(--pink-soft)"><span style="border-radius:50%"></span></div>
  <p class="txt abs" style="left:28px;top:142px;width:56px">Un jury garanti indépendant de 100 testeurs par produit pour assurer le caractère représentatif des résultats</p>
  <p class="txt abs" style="left:92px;top:122px;width:56px">Les produits testés en situation réelle par des consommateurs experts, choisis sans influence des laboratoires</p>
  <p class="txt abs" style="left:156px;top:106px;width:56px">Une note minimale de 15/20 est nécessaire pour prétendre être lauréat, et seuls les mieux notés sont récompensés</p>
  <p class="txt abs" style="left:220px;top:122px;width:58px">Seul 10% des produits d'un linéaire peuvent être distingués, ex. 40 produits, 4 pourront être lauréats</p>
  <p class="txt abs" style="left:290px;top:142px;width:60px">L'exploitation du logo est gratuite, ce qui assure la crédibilité et l'impartialité de la distinction</p>
  <div class="ft"><i></i>Verdania</div>
</section>

<!-- 8 excellence cards -->
<section class="slide" style="left:406px;top:456px">
  <div class="hd-bar"></div>
  <div class="hd"><span class="mark"></span>Une certification <em>d'excellence</em></div>
  <div class="card" style="left:23px"><div class="band" style="background:var(--pink)"></div><div class="ic" style="border-color:var(--pink-mid)"></div><p>Un jury garanti indépendant de 100 testeurs par produit pour assurer le caractère représentatif des résultats</p></div>
  <div class="card" style="left:93px;border-color:var(--teal)"><div class="band" style="background:var(--teal)"></div><div class="ic" style="border-color:var(--pink-mid)"></div><p>Les produits testés en situation réelle par des consommateurs experts les ayant choisis</p></div>
  <div class="card" style="left:163px;border-color:var(--pink-soft)"><div class="band" style="background:var(--pink-soft)"></div><p style="font-size:7px;font-weight:700;margin:8px 0 4px">15/20</p><p>Une note minimale de 15/20 est nécessaire pour prétendre être lauréat face au marché</p></div>
  <div class="card" style="left:233px;border-color:var(--pink-mid)"><div class="band" style="background:var(--pink-mid)"></div><div class="ic" style="border-color:var(--pink-mid)"></div><p>Seul 10% des produits d'un linéaire peuvent être distingués par catégorie</p></div>
  <div class="card" style="left:303px"><div class="band" style="background:var(--pink)"></div><div class="ic" style="border-color:var(--pink-mid);border-radius:50%"></div><p>L'exploitation du logo est gratuite, gage de crédibilité pour le produit</p></div>
  <div class="ft"><i></i>Verdania</div>
</section>

<!-- 9 qui peut concourir -->
<section class="slide" style="left:804px;top:456px">
  <div class="hd-bar"></div>
  <div class="hd"><span class="mark"></span>Qui peut <em>concourir?</em></div>
  <div class="abs" style="left:6px;top:72px;width:325px;height:62px;background:var(--pink-pale);border:1px solid var(--pink-soft)"></div>
  <p class="abs" style="left:48px;top:80px;font-size:4.5px;color:var(--pink);font-weight:700">Circuit GMS</p>
  <p class="txt abs" style="left:18px;top:94px;width:110px;text-align:center;color:var(--pink-mid)">Pour participer il est nécessaire que les produits présentés ne soient vendus qu'en circuit GMS.</p>
  <div class="abs" style="left:123px;top:65px;width:76px;height:76px;border-radius:50%;background:var(--teal)"></div>
  <p class="abs" style="left:128px;top:80px;width:66px;text-align:center;color:#fff;font-size:3.8px;line-height:1.35"><b style="font-size:4.5px">Marques indépendantes</b><br><br>Les marques indépendantes et les MDD peuvent désormais participer au concours.</p>
  <p class="abs" style="left:248px;top:80px;font-size:4.5px;color:var(--pink);font-weight:700">Produits labélisés</p>
  <p class="txt abs" style="left:212px;top:90px;width:115px;color:var(--pink-mid)">Cette distinction est uniquement destinée à des produits labélisés. Les labels retenus sont les labels agriculture biologique et écologiques officiels reconnus en Europe et ailleurs.</p>
  <div class="abs" style="left:338px;top:44px;width:26px;height:26px;border:1px solid #ccc"></div>
  <div class="abs" style="left:340px;top:80px;width:26px;height:26px;border-radius:50%;background:var(--pink)"></div>
  <div class="abs" style="left:340px;top:116px;width:26px;height:26px;border-radius:50%;background:#1d6d3d"></div>
  <div class="ph" role="img" aria-label="Photo de produits bio alignés : pots, bocaux et paquets" style="left:10px;top:158px;width:200px;height:44px;background:linear-gradient(90deg,#d99b3c,#b56b30,#e6d7b9,#c24b3c,#d9c8a0)"></div>
  <div class="abs" style="left:218px;top:178px;width:22px;height:22px;background:#2f9e4d"></div>
  <div class="abs" style="left:268px;top:184px;width:30px;height:12px;background:#e46b1f"></div>
  <div class="abs" style="left:328px;top:178px;width:24px;height:22px;border-radius:50%;border:2px solid #2f9e4d"></div>
  <div class="ft"><i></i>Verdania</div>
</section>

<!-- 10 déroulement -->
<section class="slide" style="left:10px;top:680px">
  <div class="hd-bar"></div>
  <div class="hd"><span class="mark"></span>Le déroulement du <em>concours</em></div>
  <div class="ph room" role="img" aria-label="Photo d'un panel de consommateurs testant les produits" style="left:82px;top:64px;width:42px;height:28px"></div>
  <div class="ph room" role="img" aria-label="Photo d'un envoi de colis aux testeurs" style="left:144px;top:64px;width:40px;height:28px"></div>
  <div class="ph room" role="img" aria-label="Capture d'un tableau de résultats" style="left:200px;top:64px;width:40px;height:28px;background:linear-gradient(#f3f3f3,#c9c9c9)"></div>
  <div class="ph room" role="img" aria-label="Photo de la cérémonie de remise des trophées" style="left:256px;top:64px;width:42px;height:28px"></div>
  <div class="logo abs" style="left:318px;top:60px;width:40px;font-size:5px"><span class="sq" style="width:24px;height:24px"></span>Palme Acheteurs Vert</div>
  <p class="abs" style="left:34px;top:100px;width:320px;display:flex;justify-content:space-between;font-size:3.6px;font-weight:700"><span>NOVEMBRE – MAI</span><span>JUIN</span><span>SEPTEMBRE</span><span>FIN OCTOBRE</span><span>DÉCEMBRE</span><span>ANNÉE SUIVANTE</span></p>
  <svg class="abs" style="left:24px;top:108px" width="340" height="36" viewBox="0 0 340 36">
    <g fill="none" stroke="#ec1b63" stroke-width="1">
      <circle cx="16" cy="18" r="8"/><circle cx="72" cy="18" r="8"/><circle cx="128" cy="18" r="8" stroke="#f46a9a"/><circle cx="184" cy="18" r="8" stroke="#f79cbd"/><circle cx="240" cy="18" r="8" stroke="#f9b9cf"/><circle cx="296" cy="18" r="8" stroke="#fbd0df"/>
    </g>
    <g font-size="6" fill="#ec1b63" text-anchor="middle" font-family="Nunito Sans"><text x="16" y="20">1</text><text x="72" y="20">2</text><text x="128" y="20">3</text><text x="184" y="20">4</text><text x="240" y="20">5</text><text x="296" y="20">6</text></g>
    <polygon points="30,4 40,4 52,18 40,32 30,32 42,18" fill="#ec1b63"/>
    <polygon points="86,4 96,4 108,18 96,32 86,32 98,18" fill="#f0427d"/>
    <polygon points="142,4 152,4 164,18 152,32 142,32 154,18" fill="#f46a9a"/>
    <polygon points="198,4 208,4 220,18 208,32 198,32 210,18" fill="#f79cbd"/>
    <polygon points="254,4 264,4 276,18 264,32 254,32 266,18" fill="#f9b9cf"/>
    <polygon points="310,4 320,4 332,18 320,32 310,32 322,18" fill="#fbd0df"/>
  </svg>
  <p class="txt abs" style="left:76px;top:150px;width:300px;display:flex;justify-content:space-between;font-weight:700"><span>Sélection des testeurs</span><span>Envoi des produits</span><span>Réception des résultats</span><span>Cérémonie de remise</span><span>Utilisation</span></p>
  <p class="txt abs" style="left:76px;top:160px;width:42px;font-style:italic">1200 consommateurs bio sont en test, sélectionnés pour tester les produits</p>
  <p class="txt abs" style="left:136px;top:160px;width:42px;font-style:italic">Les consommateurs reçoivent le produit et le testent chez eux</p>
  <p class="txt abs" style="left:192px;top:160px;width:42px;font-style:italic">Selon des critères de notation précis, par catégorie</p>
  <p class="txt abs" style="left:248px;top:160px;width:44px;font-style:italic">La soirée de remise des trophées 2018 a accueilli le monde du bio</p>
  <p class="txt abs" style="left:304px;top:160px;width:44px;font-style:italic">Exploitation gratuite du logo pendant 1 an du 1er janvier au 31 décembre</p>
  <div class="ft"><i></i>Verdania</div>
</section>

<!-- 11 participer boards -->
<section class="slide" style="left:406px;top:680px">
  <div class="hd-bar"></div>
  <div class="hd"><span class="mark"></span><em>Participer,</em> c'est...</div>
  <div class="board" style="left:14px;top:52px;width:100px;height:150px"><h4>PARTICIPANTS</h4><p>Test produit réalisé auprès d'un panel de 100 consommateurs en affinité avec votre produit</p><p>Obtenir des retours consommateurs afin d'évaluer la perception de vos produits</p><p>Les produits sont présentés lors d'une campagne de communication et de communiqués de presse</p><p>Présence à la Soirée de remise des trophées</p></div>
  <div class="board" style="left:100px;top:52px;width:100px;height:150px;left:100px"><h4>LAURÉATS</h4><p>Être identifié comme un produit bio bon et efficace : les consommateurs deviennent prescripteurs</p><p>Donner une valeur ajoutée et des arguments de vente à vos commerciaux</p><p>Un trophée avec le rappel du produit en inclusion dans du plexiglas</p></div>
  <div class="ph" role="img" aria-label="Photo de pots de pâte à tartiner au chocolat lauréats" style="left:188px;top:0;width:98px;height:120px"></div>
  <div class="ph room" role="img" aria-label="Photo de deux lauréats lors de la soirée" style="left:290px;top:0;width:93px;height:58px"></div>
  <div class="ph room" role="img" aria-label="Photo de la salle de la cérémonie" style="left:290px;top:62px;width:93px;height:58px"></div>
  <div class="ph room" role="img" aria-label="Photo du dîner de gala de remise des trophées" style="left:188px;top:124px;width:195px;height:92px;background:linear-gradient(160deg,#cfc4b4,#4a4440)"></div>
</section>

<!-- 12 participer pink -->
<section class="slide" style="left:804px;top:680px">
  <div class="hd-bar"></div>
  <div class="hd"><span class="mark"></span><em>Participer,</em> c'est...</div>
  <p class="abs" style="left:45px;top:56px;font-size:5px;text-align:center;line-height:1.1"><small style="font-size:3.5px">Et en plus</small><br>LAURÉATS</p>
  <div class="pinkbox abs" style="left:0;top:68px;width:110px;height:44px">Être identifié comme un produit bio bon et efficace : les consommateurs deviennent prescripteurs de votre produit</div>
  <div class="pinkbox abs" style="left:0;top:114px;width:110px;height:40px">Donner une valeur ajoutée et des arguments de vente à vos commerciaux et distributeurs</div>
  <div class="pinkbox abs" style="left:0;top:156px;width:110px;height:40px">Un trophée avec le rappel du produit en inclusion dans du plexiglas (idéal pour utiliser dans les salons)</div>
  <div class="ph" role="img" aria-label="Photo de pots de pâte à tartiner au chocolat" style="left:110px;top:40px;width:70px;height:155px"></div>
  <div class="ph room" role="img" aria-label="Photo de la remise des trophées" style="left:182px;top:40px;width:76px;height:155px"></div>
  <p class="abs" style="left:300px;top:30px;font-size:5px">PARTICIPANTS</p>
  <div class="pinkbox abs" style="left:258px;top:40px;width:125px;height:38px;background:var(--pink)">Test produit réalisé auprès d'un panel de 100 consommateurs en affinité avec votre produit</div>
  <div class="pinkbox abs" style="left:258px;top:80px;width:125px;height:38px">Obtenir des retours consommateurs afin d'évaluer la perception de vos produits</div>
  <div class="pinkbox abs" style="left:258px;top:120px;width:125px;height:38px">Les produits sont présentés lors d'une campagne de communication et de communiqués de presse</div>
  <div class="pinkbox abs" style="left:258px;top:160px;width:125px;height:36px;background:var(--pink-soft)">Présence à la Soirée de remise des trophées</div>
  <div class="ft"><i></i>Verdania</div>
</section>

<!-- 13 participer white -->
<section class="slide" style="left:10px;top:902px">
  <div class="hd-bar"></div>
  <div class="hd"><span class="mark"></span><em>Participer,</em> c'est...</div>
  <p class="abs" style="left:48px;top:54px;font-size:5px;text-align:center;line-height:1.1;color:var(--pink)"><small style="font-size:3.5px">Et en plus</small><br>LAURÉATS</p>
  <div class="wbox" style="left:4px;top:66px;width:114px;height:36px">Être identifié comme un produit bio bon et efficace : les consommateurs deviennent prescripteurs de votre produit</div>
  <div class="wbox" style="left:4px;top:106px;width:114px;height:36px">Donner une valeur ajoutée et des arguments de vente à vos commerciaux et distributeurs</div>
  <div class="wbox" style="left:4px;top:146px;width:114px;height:36px">Un trophée avec le rappel du produit en inclusion dans du plexiglas</div>
  <div class="ph" role="img" aria-label="Photo de pots de pâte à tartiner au chocolat" style="left:116px;top:38px;width:70px;height:155px"></div>
  <div class="ph room" role="img" aria-label="Photo de la cérémonie de remise des trophées" style="left:188px;top:38px;width:80px;height:155px"></div>
  <p class="abs" style="left:302px;top:28px;font-size:5px;color:var(--pink)">PARTICIPANTS</p>
  <div class="wbox" style="left:266px;top:38px;width:114px;height:34px">Test produit réalisé auprès d'un panel de 100 consommateurs en affinité avec votre produit</div>
  <div class="wbox" style="left:266px;top:76px;width:114px;height:34px">Obtenir des retours consommateurs afin d'évaluer la perception de vos produits</div>
  <div class="wbox" style="left:266px;top:114px;width:114px;height:36px">Les produits sont présentés lors d'une campagne de communication et de presse</div>
  <div class="wbox" style="left:266px;top:154px;width:114px;height:36px;padding-top:13px">Présence à la Soirée de remise des trophées</div>
  <div class="ft"><i></i>Verdania</div>
</section>

<!-- 14 visibilité wheel -->
<section class="slide" style="left:406px;top:902px">
  <div class="hd-bar"></div>
  <div class="hd"><span class="mark"></span>Participer, c'est...</div>
  <svg class="abs" style="left:136px;top:50px" width="110" height="110" viewBox="0 0 110 110">
    <circle cx="55" cy="55" r="52" fill="#f79cbd"/>
    <g stroke="#fff" stroke-width="3">
      <line x1="55" y1="3" x2="55" y2="107"/><line x1="3" y1="55" x2="107" y2="55"/>
      <line x1="18" y1="18" x2="92" y2="92"/><line x1="92" y1="18" x2="18" y2="92"/>
    </g>
    <circle cx="55" cy="55" r="36" fill="#ec1b63"/>
    <circle cx="55" cy="55" r="26" fill="#fff"/><circle cx="55" cy="55" r="24" fill="#f9b9cf"/>
    <text x="55" y="50" font-size="4" fill="#fff" text-anchor="middle" font-family="Nunito Sans">Visibilité accrue</text>
    <text x="55" y="56" font-size="4" fill="#fff" text-anchor="middle" font-family="Nunito Sans">des lauréats grâce</text>
    <text x="55" y="62" font-size="4" fill="#fff" text-anchor="middle" font-family="Nunito Sans">à une campagne</text>
  </svg>
  <p class="txt abs" style="left:160px;top:40px;width:60px;text-align:center">Relation presse toute l'année</p>
  <p class="txt abs" style="left:78px;top:62px;width:40px">En magasin (stop-rayon...)</p>
  <div class="abs" role="img" aria-label="Borne d'affichage en magasin" style="left:40px;top:58px;width:30px;height:62px;background:linear-gradient(#3a3a3a,#777)"></div>
  <div class="logo abs" style="left:80px;top:82px;width:46px;font-size:5px"><span class="sq" style="width:24px;height:24px"></span>Palme Acheteurs Vert</div>
  <p class="txt abs" style="left:76px;top:146px;width:60px;text-align:center">Mise en avant des lauréats 2019 lors du salon Organexpo</p>
  <p class="abs" style="left:76px;top:168px;font-size:8px;font-weight:700;color:#6a6a2a">ORGANEXPO<span style="color:var(--pink)">2019</span></p>
  <p class="txt abs" style="left:250px;top:72px;width:40px;text-align:center">Cérémonie de remise des trophées</p>
  <div class="ph room" role="img" aria-label="Photo de la cérémonie" style="left:296px;top:40px;width:52px;height:34px;border:3px solid #fff;box-shadow:0 1px 3px rgba(0,0,0,.3)"></div>
  <div class="abs" style="left:294px;top:100px;width:60px;height:56px;background:var(--pink);padding:5px"><div role="img" aria-label="Capture d'un site internet sur ordinateur portable" style="width:50px;height:30px;background:linear-gradient(#444,#888)"></div><p style="font-size:3px;color:#fff;margin-top:4px;text-align:center">Sites et newsletters dédiés</p></div>
  <p class="txt abs" style="left:232px;top:128px;width:60px;text-align:center">Sites Internet et newsletters dédiées</p>
  <p class="txt abs" style="left:172px;top:186px;width:40px;text-align:center">Réseaux sociaux</p>
  <div class="abs" style="left:182px;top:194px;width:10px;height:10px;background:#3b5998"></div>
  <div class="abs" style="left:196px;top:194px;width:10px;height:10px;background:var(--pink)"></div>
  <div class="ft"><i></i>Verdania</div>
</section>

<!-- 15 contact -->
<section class="slide" style="left:804px;top:902px">
  <div class="hd-bar"></div>
  <div class="hd"><span class="mark"></span>Participer, c'est...</div>
  <p class="abs" style="left:14px;top:72px;font-size:6px;line-height:2">Date limite d'inscription des produits :<br>le 10 Juillet 2019</p>
  <div class="abs" style="left:0;top:104px;width:280px;height:22px;background:var(--pink);color:#fff;font-size:7px;font-weight:700;padding:6px 14px">Contactez-nous</div>
  <div class="abs" style="left:280px;top:104px;width:103px;height:22px;background:var(--pink)"></div>
  <div class="abs" style="left:286px;top:90px;width:80px;height:80px;background:#fff;border-radius:8px;box-shadow:0 2px 4px rgba(0,0,0,.2)"></div>
  <div class="logo abs" style="left:290px;top:94px;width:72px;font-size:8px"><span class="sq"></span>Palme Acheteurs Vert</div>
  <svg class="abs" style="left:12px;top:144px" width="16" height="50" viewBox="0 0 16 50" fill="#ec1b63">
    <path d="M3 1 L7 1 L8 6 L6 8 Q8 12 11 14 L13 12 L16 13 L16 17 Q6 18 1 5 Z"/>
    <rect x="1" y="32" width="14" height="14" rx="2" fill="none" stroke="#ec1b63" stroke-width="1.5"/><rect x="4" y="36" width="8" height="3"/>
  </svg>
  <p class="abs" style="left:34px;top:149px;font-size:5px">01 00 00 11 22</p>
  <p class="abs" style="left:34px;top:179px;font-size:5px">01 00 00 33 44</p>
  <svg class="abs" style="left:120px;top:144px" width="16" height="50" viewBox="0 0 16 50">
    <rect x="1" y="3" width="14" height="10" fill="#ec1b63"/><polyline points="1,3 8,9 15,3" fill="none" stroke="#fff"/>
    <circle cx="8" cy="40" r="7" fill="none" stroke="#ec1b63" stroke-width="1.3"/><ellipse cx="8" cy="40" rx="3" ry="7" fill="none" stroke="#ec1b63"/><line x1="1" y1="40" x2="15" y2="40" stroke="#ec1b63"/>
  </svg>
  <p class="abs" style="left:143px;top:149px;font-size:5px;color:#1a55c9;text-decoration:underline">contact@palme-vert.example</p>
  <p class="abs" style="left:143px;top:176px;font-size:5px;color:#1a55c9;text-decoration:underline;line-height:1.5">www.palme-vert.example<br>www.verdania.example</p>
  <div class="ft"><i></i>Verdania</div>
</section>

</body>
</html>
```